Tolvern Business Cards

Business card design. dont mind if new logo is suggested.
it would be for a security company.
our clients would be bigger security companies around Australia.
have a logo done but can be replaced. see attaached. like the colors.
Need company name, person name, designation, phone and email on front.
At back company logo and name. website saddress and 2 x license numbers
would like to have 2 different background color for both sidde

Industry/Entity Type

Security

Contact Information for Business Card

round corners, front should be light in color. need logo at back with webaddress and 2 x license numners

Font styles to use
Sans Serif

Colors
f37122
faa54b
f8ba93
0255a3
0592cd
85cae6
b3d448
9bcb3c
ffffff

Requirements
Must have
• see description
Nice to have
• see description
Should not have
• should not be difficult to read or hardd to find information on card.. lets say easy on eyes yet catchy

```html
<!DOCTYPE html>
<html lang="en">
<head>
<meta charset="utf-8">
<title>Tolvern Business Cards</title>
<link rel="stylesheet" href="https://fonts.googleapis.com/css2?family=Tenor+Sans&display=swap">
<style>
  :root {
    --board: #b2b2b0;
    --card: #ffffff;
    --navy: #1d3461;
    --green: #72bf44;
    --orange: #f37122;
    --font: "Tenor Sans", sans-serif;
  }
  * { margin: 0; padding: 0; box-sizing: border-box; }
  html, body { width: 1200px; height: 848px; overflow: hidden; }
  body { background: var(--board); font-family: var(--font); position: relative; }

  .card {
    position: absolute;
    width: 362px;
    height: 218px;
    background: var(--card);
    border-radius: 14px;
    overflow: hidden;
    box-shadow: 0 1px 3px rgba(0,0,0,0.12);
  }
  .card svg.shapes { position: absolute; inset: 0; width: 100%; height: 100%; }

  .theme-navy { --accent: var(--navy); }
  .theme-green { --accent: var(--green); }
  .theme-orange { --accent: var(--orange); }

  .shape { fill: var(--accent); }

  /* front */
  .front .brand {
    position: absolute;
    left: 164px;
    top: 72px;
    font-size: 13px;
    letter-spacing: 0.2px;
    color: var(--accent);
    white-space: nowrap;
  }

  /* back */
  .back .brand {
    position: absolute;
    left: 0;
    width: 200px;
    top: 148px;
    text-align: center;
    font-size: 9.5px;
    color: var(--accent);
    white-space: nowrap;
  }
  .back .divider {
    position: absolute;
    left: 181px;
    top: 31px;
    width: 1px;
    height: 163px;
    background: var(--accent);
  }
  .back .contact {
    position: absolute;
    left: 197px;
    top: 52px;
    list-style: none;
    font-size: 7.6px;
    line-height: 12px;
    color: var(--accent);
    white-space: nowrap;
  }
  .theme-navy .contact { color: var(--navy); }
</style>
</head>
<body>

  <!-- front row -->
  <section class="card front theme-navy" style="left:44px; top:158px;">
    <svg class="shapes" viewBox="0 0 362 218" aria-hidden="true">
      <circle class="shape" cx="84" cy="70" r="22"/>
      <circle class="shape" cx="85" cy="137" r="14"/>
      <circle class="shape" cx="148" cy="160" r="20"/>
      <circle class="shape" cx="234" cy="184" r="27"/>
      <circle class="shape" cx="343" cy="212" r="46"/>
    </svg>
    <p class="brand">TOLVERN SECURITY GROUP</p>
  </section>

  <section class="card front theme-green" style="left:422px; top:158px;">
    <svg class="shapes" viewBox="0 0 362 218" aria-hidden="true">
      <circle class="shape" cx="84" cy="70" r="22"/>
      <circle class="shape" cx="85" cy="137" r="14"/>
      <circle class="shape" cx="148" cy="160" r="20"/>
      <circle class="shape" cx="234" cy="184" r="27"/>
      <circle class="shape" cx="343" cy="212" r="46"/>
    </svg>
    <p class="brand">TOLVERN SECURITY GROUP</p>
  </section>

  <section class="card front theme-orange" style="left:799px; top:158px;">
    <svg class="shapes" viewBox="0 0 362 218" aria-hidden="true">
      <circle class="shape" cx="84" cy="70" r="22"/>
      <circle class="shape" cx="85" cy="137" r="14"/>
      <circle class="shape" cx="148" cy="160" r="20"/>
      <circle class="shape" cx="234" cy="184" r="27"/>
      <circle class="shape" cx="343" cy="212" r="46"/>
    </svg>
    <p class="brand">TOLVERN SECURITY GROUP</p>
  </section>

  <!-- back row -->
  <section class="card back theme-navy" style="left:44px; top:451px;">
    <svg class="shapes" viewBox="0 0 362 218" aria-hidden="true">
      <circle class="shape" cx="-40" cy="-40" r="130"/>
      <circle class="shape" cx="402" cy="258" r="125"/>
      <circle class="shape" cx="100" cy="102" r="26"/>
    </svg>
    <p class="brand">TOLVERN SECURITY GROUP</p>
    <span class="divider"></span>
    <ul class="contact">
      <li>Mr Alan Reeve</li>
      <li>Position</li>
      <li>Licence number 1</li>
      <li>Licence number 2</li>
      <li>www.tolvernsecuritygroup.com.au</li>
      <li>14 Carlow street NSW 2040</li>
      <li>areeve@tolvernsecurity.com.au</li>
      <li>0400 117 258</li>
    </ul>
  </section>

  <section class="card back theme-green" style="left:420px; top:451px;">
    <svg class="shapes" viewBox="0 0 362 218" aria-hidden="true">
      <circle class="shape" cx="-40" cy="-40" r="130"/>
      <circle class="shape" cx="402" cy="258" r="125"/>
      <circle class="shape" cx="100" cy="102" r="26"/>
    </svg>
    <p class="brand">TOLVERN SECURITY GROUP</p>
    <span class="divider"></span>
    <ul class="contact">
      <li>Mr Alan Reeve</li>
      <li>Position</li>
      <li>Licence number 1</li>
      <li>Licence number 2</li>
      <li>www.tolvernsecuritygroup.com.au</li>
      <li>14 Carlow street NSW 2040</li>
      <li>areeve@tolvernsecurity.com.au</li>
      <li>0400 117 258</li>
    </ul>
  </section>

  <section class="card back theme-orange" style="left:795px; top:451px;">
    <svg class="shapes" viewBox="0 0 362 218" aria-hidden="true">
      <circle class="shape" cx="-40" cy="-40" r="130"/>
      <circle class="shape" cx="402" cy="258" r="125"/>
      <circle class="shape" cx="100" cy="102" r="26"/>
    </svg>
    <p class="brand">TOLVERN SECURITY GROUP</p>
    <span class="divider"></span>
    <ul class="contact">
      <li>Mr Alan Reeve</li>
      <li>Position</li>
      <li>Licence number 1</li>
      <li>Licence number 2</li>
      <li>www.tolvernsecuritygroup.com.au</li>
      <li>14 Carlow street NSW 2040</li>
      <li>areeve@tolvernsecurity.com.au</li>
      <li>0400 117 258</li>
    </ul>
  </section>

</body>
</html>
```